Stationery Design for Family Law Firm
BROOK VESTAL, LLP
Stationery Design for Family Law Firm -
Creative Brief
Professional
Martin D. Vestal
Attorney & Counselor at Law
4187 Larkin Street San Diego, CA 92104
martin@brookvestal-law.example
www.brookvestal-law.example
Paper will be ivory. Please use large and small caps for name and "Attorney & Counselor" at Law. Sentence case for the rest.
Family Law I Guardianships I Conservatorships I Estate Planning

```html
<!DOCTYPE html>
<html lang="en">
<head>
<meta charset="utf-8">
<title>Brook Vestal, LLP — Business Cards</title>
<link href="https://fonts.googleapis.com/css2?family=Cinzel:wght@500&family=Cormorant+SC:wght@500;600&display=swap" rel="stylesheet">
<style>
  :root {
    --backdrop: #3a3b3d;
    --ivory: #fbfaf6;
    --ivory-shade: #e9e8e3;
    --night: #0c0c0d;
    --night-shade: #2a2b2e;
    --firm-blue: #2d6fb3;
    --band-blue: #2a65a8;
    --band-grey: #4a4b4e;
    --ink: #2b2b2b;
    --paper-text: #f2f2f2;
  }
  * { margin: 0; padding: 0; box-sizing: border-box; }
  html, body { width: 1200px; height: 736px; overflow: hidden; }
  body { background: var(--backdrop); position: relative; font-family: "Cormorant SC", Georgia, serif; }

  .card {
    position: absolute; width: 542px; height: 300px; border-radius: 14px; overflow: hidden;
    box-shadow: 0 6px 18px rgba(0,0,0,.45);
  }
  .card--ivory { background: linear-gradient(180deg, var(--ivory) 0%, var(--ivory-shade) 100%); color: var(--ink); }
  .card--night { background: radial-gradient(ellipse at 60% 35%, var(--night-shade) 0%, var(--night) 70%); color: var(--paper-text); }
  .front-top-left { left: 44px; top: 66px; }
  .back-top-right { left: 614px; top: 66px; }
  .front-bottom-left { left: 44px; top: 388px; }
  .back-bottom-right { left: 614px; top: 388px; }

  .firm-mark { position: absolute; text-align: center; }
  .firm-name { font-family: "Cinzel", Georgia, serif; font-weight: 500; color: var(--firm-blue); letter-spacing: .5px; white-space: nowrap; }
  .firm-tagline { font-weight: 600; letter-spacing: .6px; margin-top: 4px; white-space: nowrap; }
  .card--night .firm-name { color: var(--paper-text); }

  .front .firm-mark { left: 170px; top: 44px; width: 280px; }
  .front .firm-name { font-size: 25px; }
  .front .firm-tagline { font-size: 12px; }

  .back .firm-mark { left: 0; width: 100%; top: 92px; }
  .back .firm-name { font-size: 40px; }
  .back .firm-tagline { font-size: 17px; }
  .back-bottom-right .firm-mark { top: 80px; }
  .back-bottom-right .firm-name { font-size: 44px; }

  .contact { position: absolute; left: 18px; top: 152px; width: 250px; font-size: 12px; line-height: 16px; font-weight: 500; }
  .contact p { white-space: nowrap; }

  .person { position: absolute; left: 284px; top: 170px; }
  .person-name { font-size: 24px; color: var(--firm-blue); font-weight: 500; line-height: 1; white-space: nowrap; }
  .person-title { font-size: 13px; font-weight: 600; letter-spacing: .3px; margin-top: 3px; white-space: nowrap; }

  .practice-areas {
    position: absolute; left: 0; width: 100%; top: 196px; text-align: center;
    font-size: 16px; font-weight: 600; letter-spacing: .3px; white-space: nowrap;
  }
  .card--ivory .practice-areas { color: var(--firm-blue); }
  .back-bottom-right .practice-areas { top: 208px; }

  .swoosh { position: absolute; left: 0; bottom: 0; width: 542px; height: 300px; }
</style>
</head>
<body>

  <section class="card card--ivory front front-top-left">
    <svg class="swoosh" viewBox="0 0 542 300" aria-hidden="true">
      <path d="M170 300 C290 264 430 240 542 214 L542 240 C430 264 310 286 220 300 Z" fill="var(--band-grey)"/>
      <path d="M0 278 C170 272 370 256 542 222 L542 300 L0 300 Z" fill="var(--band-blue)" opacity=".92"/>
      <path d="M0 292 C180 286 380 268 542 240 L542 300 L0 300 Z" fill="var(--band-blue)"/>
    </svg>
    <div class="firm-mark">
      <div class="firm-name">Brook Vestal, LLP</div>
      <div class="firm-tagline">Attorneys &amp; Counselors at Law</div>
    </div>
    <div class="contact">
      <p>4187 Larkin Street</p>
      <p>San Diego, CA 92104</p>
      <p>Phone: (619) 555-0142</p>
      <p>Email: martin@brookvestal-law.example</p>
      <p>Web: www.brookvestal-law.example</p>
    </div>
    <div class="person">
      <div class="person-name">Martin D. Vestal</div>
      <div class="person-title">Attorney &amp; Counselor at Law</div>
    </div>
  </section>

  <section class="card card--ivory back back-top-right">
    <div class="firm-mark">
      <div class="firm-name">Brook Vestal, LLP</div>
      <div class="firm-tagline">Attorneys &amp; Counselors at Law</div>
    </div>
    <p class="practice-areas">Family Law | Guardianships | Conservatorships | Estate Planning</p>
  </section>

  <section class="card card--night front front-bottom-left">
    <svg class="swoosh" viewBox="0 0 542 300" aria-hidden="true">
      <path d="M170 300 C290 266 430 242 542 216 L542 242 C430 266 310 288 220 300 Z" fill="var(--band-grey)"/>
      <path d="M0 280 C170 274 370 258 542 224 L542 300 L0 300 Z" fill="var(--band-blue)" opacity=".9"/>
      <path d="M0 293 C180 288 380 270 542 242 L542 300 L0 300 Z" fill="var(--band-blue)"/>
    </svg>
    <div class="firm-mark">
      <div class="firm-name">Brook Vestal, LLP</div>
      <div class="firm-tagline">Attorneys &amp; Counselors at Law</div>
    </div>
    <div class="contact">
      <p>4187 Larkin Street</p>
      <p>San Diego, CA 92104</p>
      <p>Phone: (619) 555-0142</p>
      <p>Email: martin@brookvestal-law.example</p>
      <p>Web: www.brookvestal-law.example</p>
    </div>
    <div class="person">
      <div class="person-name">Martin D. Vestal</div>
      <div class="person-title">Attorney &amp; Counselor at Law</div>
    </div>
  </section>

  <section class="card card--night back back-bottom-right">
    <div class="firm-mark">
      <div class="firm-name">Brook Vestal, LLP</div>
      <div class="firm-tagline">Attorneys &amp; Counselors at Law</div>
    </div>
    <p class="practice-areas">Family Law | Guardianships | Conservatorships | Estate Planning</p>
  </section>

</body>
</html>
```